Business Card For Kelmora Financial Consulting

Hi, I would like a business card designed. Bold, modern.
Please use the same design as the logo. I have also attached the website design to see the overall theme.
Wordmark Font
Color: Hex: #01AEF7

```html
<!DOCTYPE html>
<html lang="en">
<head>
<meta charset="utf-8">
<title>Kelmora Financial Consulting – Business Card</title>
<link rel="stylesheet" href="https://fonts.googleapis.com/css2?family=Poppins:wght@400;600&display=swap">
<style>
  :root {
    --bg: #8a8a8a;
    --card-front: #ffffff;
    --card-back: #16232e;
    --navy: #0b4670;
    --sky: #01aef7;
    --ink: #1a1a1a;
    --rule: #cfcfcf;
    --back-mark: #2c5f86;
  }
  * { box-sizing: border-box; margin: 0; padding: 0; }
  html, body { width: 1093px; height: 1200px; overflow: hidden; }
  body {
    background: var(--bg);
    font-family: "Poppins", sans-serif;
    position: relative;
  }
  .card {
    position: absolute;
    left: 265px;
    width: 577px;
    height: 356px;
    border-radius: 27px;
  }
  .card--front { top: 226px; background: var(--card-front); }
  .card--back { top: 621px; background: var(--card-back); }

  .brand {
    position: absolute;
    display: flex;
    align-items: center;
    gap: 10px;
    font-weight: 600;
    color: var(--navy);
  }
  .brand__square {
    width: 40px; height: 40px;
    border: 3px solid var(--sky);
  }
  .brand__name { font-size: 30px; line-height: 1; letter-spacing: 2px; }
  .brand__sub { font-size: 9px; letter-spacing: 4.4px; margin-top: 6px; }
  .card--front .brand { right: 31px; top: 68px; }
  .card--back .brand { left: 50%; top: 50%; transform: translate(-50%, -50%); color: var(--back-mark); gap: 12px; }
  .card--back .brand__square { width: 50px; height: 50px; border-color: #0a0f14; }
  .card--back .brand__name { font-size: 38px; }
  .card--back .brand__sub { font-size: 11px; letter-spacing: 6.4px; }

  .person { position: absolute; left: 26px; top: 188px; }
  .person__name { font-weight: 600; font-size: 23px; color: var(--navy); line-height: 1.1; }
  .person__title { font-size: 14.5px; color: var(--sky); letter-spacing: 1px; line-height: 1.2; }

  .divider {
    position: absolute; left: 26px; right: 31px; top: 243px;
    border-top: 1px solid var(--rule);
  }

  .contacts { position: absolute; left: 26px; top: 261px; list-style: none; }
  .contacts li {
    display: flex; align-items: center; gap: 7px;
    font-size: 17px; color: var(--ink); line-height: 21px;
  }
  .contacts svg { width: 16px; height: 16px; fill: var(--ink); flex: none; }
  .contacts .accent { color: var(--sky); }

  .address {
    position: absolute; right: 31px; top: 282px;
    text-align: right; font-style: normal;
    font-size: 17px; line-height: 21px; color: var(--ink);
  }
</style>
</head>
<body>
  <section class="card card--front" aria-label="Business card front">
    <div class="brand">
      <span class="brand__square"></span>
      <div>
        <div class="brand__name">KELMORA</div>
        <div class="brand__sub">FINANCIAL CONSULTING</div>
      </div>
    </div>

    <div class="person">
      <h1 class="person__name">DANIEL HARLOW</h1>
      <p class="person__title">MANAGING DIRECTOR</p>
    </div>

    <div class="divider"></div>

    <ul class="contacts">
      <li>
        <svg viewBox="0 0 24 24" aria-hidden="true"><path d="M6.6 10.8a15.1 15.1 0 0 0 6.6 6.6l2.2-2.2a1 1 0 0 1 1-.25 11.4 11.4 0 0 0 3.6.57 1 1 0 0 1 1 1V20a1 1 0 0 1-1 1A17 17 0 0 1 3 4a1 1 0 0 1 1-1h3.5a1 1 0 0 1 1 1c0 1.25.2 2.45.57 3.57a1 1 0 0 1-.25 1z"/></svg>
        044-555 018 234
      </li>
      <li>
        <svg viewBox="0 0 24 24" aria-hidden="true"><path d="M2 5h20v14H2z M3 6l9 7 9-7" fill="none" stroke="#1a1a1a" stroke-width="0"/><path d="M2 5h20v1.5l-10 7-10-7z M2 8.5l6.5 4.5L2 18z M22 8.5v9.5l-6.5-5z M9.8 14l2.2 1.5 2.2-1.5 7.8 5H2z"/></svg>
        info@kelmoraconsult.com
      </li>
      <li>
        <svg viewBox="0 0 24 24" aria-hidden="true"><circle cx="12" cy="12" r="9.5" fill="none" stroke="#1a1a1a" stroke-width="2"/><ellipse cx="12" cy="12" rx="4" ry="9.5" fill="none" stroke="#1a1a1a" stroke-width="1.6"/><path d="M2.5 9h19M2.5 15h19M12 2.5v19" stroke="#1a1a1a" stroke-width="1.6"/></svg>
        <span>www.<span class="accent">kelmoraconsult</span>.com</span>
      </li>
    </ul>

    <address class="address">
      17, Harbour Lane Suite 4<br>
      30918, Northvale
    </address>
  </section>

  <section class="card card--back" aria-label="Business card back">
    <div class="brand">
      <span class="brand__square"></span>
      <div>
        <div class="brand__name">KELMORA</div>
        <div class="brand__sub">FINANCIAL CONSULTING</div>
      </div>
    </div>
  </section>
</body>
</html>
```